Inspirational Quote Poster for Employees

For this project, we need a simple yet high-impact poster template that will be customized for each of our employees with a personalized inspirational quote and color scheme. This template should allow us to quickly and easily customize the text and colors in the poster without a lot of effort.

The poster design should consist of:
- A stylized text area to contain the main text of the quote
- A separate text area to contain the source of quote
- A background that complements the color and style of the text

Text may use different typographic effects (such as color, stroke weight, italicization, font size changes, drop shadows) to draw attention to words in the quote; the source of the quote may be formatted the same as the main text of the quote, or may be formatted differently to distinguish it from the main quote.

The background may be simply a single color, subtle texture, gradients, halftone effects, or other color/texture effects may be used to complement the text.

Examples of the types of posters envisioned by this project:
- http://www.pinvelora.example/marcusdtelford/quillbase-job-1/

Sample quotes to use to build your poster - choose whichever one you want, but be certain that the poster design will handle both long and short quotes:
- "Happiness in intelligent people is the rarest thing I know" - Walden Prosket
- "Wanting to be someone else is a waste of the person you are." - Rolf Dintey
- "Experience is not what happens to you. It is what you do with what happens to you." - Ferris Mundell
- "Simplicity is the ultimate in sophistication." - Rinaldo de Pavesco
- "You will get all you want in life if you help enough other people get what they want." - Tad Pomfrey
- "Hell, there are no rules here — we're trying to accomplish something." - Gareth Vullane

Industry/Entity Type

Quote

Requirements
Must have
• Final deliverable must be:
• - Formatted for an 18” x 24” poster (in portrait orientation)
• - Delivered in Adobe InDesign, Adobe Illustrator, or Extended PostScript format
• - Use CMYK color mode
• - Be print-ready at 300dpi resolution
• - Include any fonts used in the template

```html
<!DOCTYPE html>
<html lang="en">
<head>
<meta charset="utf-8">
<title>Quote Poster – Tad Pomfrey</title>
<link rel="stylesheet" href="https://fonts.googleapis.com/css2?family=Archivo:wght@800&display=swap">
<style>
  :root {
    --poster-bg: #c8cf4f;
    --quote-mark: #55ff5e;
    --quote-ink: #c41e3a;
  }
  html, body {
    margin: 0;
    padding: 0;
    overflow: hidden;
    background: var(--poster-bg);
  }
  .poster {
    position: relative;
    width: 927px;
    height: 1200px;
    background: var(--poster-bg);
    overflow: hidden;
    font-family: "Archivo", "Helvetica Neue", Arial, sans-serif;
    font-weight: 800;
  }
  .quote-marks {
    position: absolute;
    inset: 0;
    width: 927px;
    height: 1200px;
  }
  .quote-marks path { fill: var(--quote-mark); }
  .quote-text {
    position: absolute;
    left: 20px;
    top: 192px;
    width: 880px;
    margin: 0;
    text-align: center;
    color: var(--quote-ink);
    font-size: 90px;
    line-height: 106px;
    letter-spacing: -1px;
    transform: rotate(-4deg);
    transform-origin: 50% 50%;
  }
  .quote-text span { display: block; white-space: nowrap; }
  .quote-source {
    position: absolute;
    right: 82px;
    top: 938px;
    margin: 0;
    color: var(--quote-ink);
    font-size: 86px;
    line-height: 1;
    letter-spacing: -1px;
  }
</style>
</head>
<body>
<main class="poster">
  <svg class="quote-marks" viewBox="0 0 927 1200" aria-hidden="true">
    <defs>
      <path id="mark" d="M220,82 C150,92 105,145 92,205 L70,298 L183,316 L198,212 L138,204 C150,160 180,132 216,126 Z"/>
    </defs>
    <g class="open-quote">
      <use href="#mark"/>
      <use href="#mark" transform="translate(150,25)"/>
    </g>
    <g class="close-quote">
      <use href="#mark" transform="rotate(180 435 450) translate(-300,-220)"/>
      <use href="#mark" transform="rotate(180 435 450) translate(-450,-245)"/>
    </g>
  </svg>

  <blockquote class="quote-text">
    <span>You will get all</span>
    <span>you want in life if</span>
    <span>you help enough</span>
    <span>other people get</span>
    <span>what they want.</span>
  </blockquote>

  <p class="quote-source">-Tad Pomfrey</p>
</main>
</body>
</html>
```